Birchby Candles, Hand-poured scented soy candles

Create a logo and label design to use on my vintage country farmhouse style, all natural, hand poured soy candle jars and apothecaries. Candles will be labeled in 4 different sizes so design must be adaptable, clean, simple, telegraphic and invoke interest in the product. Think Black lettering on white or black on kraft brown. 603 is the area code for New Hampshire where we make them. The labels will need a prominent area for the scent of the candle to be listed that the eyes are drawn to. Primitive country in design? Use of state attractions? Jars are a square mason style 8 ounce and 16 ounce. Tarts are a clamshell. Lids are a 70-400 series 2.5" label area. Candles are white in a clear glass jar, black lids. There will be label design sizes of 3"x 2.5" 2.5" round, 1.5"x2.5"

Target Market(s)

primitive country, farmhouse, vintage, general home decor

Contact Information for Business Card

Birchby Candles, all natural soy candles, hand-poured in New Hampshire, logo, phone, address. Possibly match the main label.

Logo Text

Birchby Candles, all natural soy candles, hand-poured in New Hampshire, area for scent description and size of container.

Font styles to use
Serif
Script

Colors

Designer to choose colors to be used in the design.

Requirements
Must have
• simple and clean, country farmhouse with a bit of vintage thrown in. possibly multiple fonts to distinguish info from scent name
Nice to have
• at this time I am open to suggestions
• Prefer scent names or brand name in an older script?
• older copperplate/Spencerian?
Should not have
• cluttered, busy, too modern, multiple colors

```html
<!DOCTYPE html>
<html lang="en">
<head>
<meta charset="utf-8">
<title>Birchby Candles – Potpourri Label</title>
<link href="https://fonts.googleapis.com/css2?family=EB+Garamond:wght@400;600;700&family=IM+Fell+English:ital@1&display=swap" rel="stylesheet">
<style>
  :root {
    --page: #f2f2f0;
    --ink: #111111;
    --paper: #ffffff;
    --paper-shade: #e6e6e6;
    --band-text: #ffffff;
  }
  html, body {
    margin: 0;
    width: 1200px;
    height: 1199px;
    overflow: hidden;
    background: var(--page);
  }
  .label {
    display: block;
    width: 1200px;
    height: 1199px;
  }
  .brand-name {
    font-family: "EB Garamond", Georgia, serif;
    font-weight: 700;
    font-size: 66px;
    fill: var(--ink);
  }
  .scent-name {
    font-family: "IM Fell English", "EB Garamond", serif;
    font-style: italic;
    font-size: 158px;
    fill: var(--ink);
  }
  .tagline {
    font-family: "EB Garamond", Georgia, serif;
    font-weight: 700;
    font-size: 44px;
    fill: var(--band-text);
  }
  .description {
    font-family: "EB Garamond", Georgia, serif;
    font-weight: 600;
    font-size: 20px;
    fill: var(--ink);
  }
  .origin {
    font-family: "EB Garamond", Georgia, serif;
    font-weight: 400;
    font-size: 32px;
    fill: var(--ink);
  }
</style>
</head>
<body>
<svg class="label" viewBox="0 0 1200 1199" xmlns="http://www.w3.org/2000/svg">
  <defs>
    <radialGradient id="label-sheen" cx="45%" cy="40%" r="70%">
      <stop offset="0%" stop-color="var(--paper)"/>
      <stop offset="75%" stop-color="var(--paper)"/>
      <stop offset="100%" stop-color="var(--paper-shade)"/>
    </radialGradient>
    <clipPath id="inner-area">
      <circle cx="600" cy="600" r="400"/>
    </clipPath>
    <path id="origin-arc" d="M 215 600 A 385 385 0 0 0 985 600"/>
  </defs>

  <!-- label disc -->
  <circle cx="600" cy="600" r="436" fill="url(#label-sheen)"/>
  <circle class="outer-ring" cx="600" cy="600" r="428" fill="none" stroke="var(--ink)" stroke-width="14"/>
  <circle class="inner-ring" cx="600" cy="600" r="400" fill="none" stroke="var(--ink)" stroke-width="4"/>

  <!-- brand -->
  <circle cx="376" cy="400" r="9" fill="var(--ink)"/>
  <text class="brand-name" x="612" y="422" text-anchor="middle">Birchby Candles</text>

  <!-- scent -->
  <text class="scent-name" x="600" y="618" text-anchor="middle">Potpourri</text>

  <!-- tagline band -->
  <g clip-path="url(#inner-area)">
    <rect x="150" y="672" width="900" height="4" fill="var(--ink)"/>
    <rect x="150" y="682" width="900" height="62" fill="var(--ink)"/>
  </g>
  <text class="tagline" x="600" y="728" text-anchor="middle">All Natural Soy Candles</text>

  <!-- scent description -->
  <g class="description" text-anchor="middle">
    <text x="600" y="785">Lorem ipsum dolor sit amet, consectetur</text>
    <text x="600" y="809">adipiscing elit, sed do eiusmod tempor</text>
    <text x="600" y="833">incididunt ut labore et dolore magna aliqua.</text>
    <text x="600" y="857">Ut enim ad minim veniam, quis nostrud</text>
    <text x="600" y="881">exercitation ullamco laboris.</text>
  </g>

  <!-- origin line -->
  <text class="origin">
    <textPath href="#origin-arc" startOffset="50%" text-anchor="middle">Hand-poured in New Hampshire</textPath>
  </text>
</svg>
</body>
</html>
```